Business Insurance for local SMEs (Small Medium Enterprises)

I am from Silver Harbour Wealth Planners (http://www.silverharbourwp.com.sg/shwp/index.html)
We need flyer design to penetrate into local market, to educate and advice business owners on Business Insurance. Areas like
- Business Succession
- Employee Benefit
- Corporate Business Insurance
Mainly is to deal with business risk management, minimise any potential business loss and thus, improving their business profit margin.

Target Market(s)

Local SME (Small Medium Enterprises) Business Owners

Industry/Entity Type

Business

Font styles to use
Serif

Colors
3377b5

Requirements
Must have
• Updates as of 31/March/2015-
• Its a 2-fold, A5 size brochure - please see attached for reference on the layout
• Please do include company logo (Planners' Circlet), as per attached.
Should not have
• Please remove Silver Harbour Wealth Planners Logo

```html
<!DOCTYPE html>
<html lang="en">
<head>
<meta charset="utf-8">
<title>Planners' Circlet – Business Insurance Brochure</title>
<link rel="stylesheet" href="https://fonts.googleapis.com/css2?family=Oswald:wght@400;500&family=Open+Sans:ital,wght@0,400;0,600;1,400&display=swap">
<style>
  :root {
    --board: #2b2b2b;
    --brand-blue: #3377b5;
    --deep-blue: #1f5d9c;
    --ink: #2e2e2e;
    --body-ink: #3c3c3c;
    --paper: #ffffff;
    --night: #111111;
    --white: #ffffff;
  }
  * { box-sizing: border-box; margin: 0; padding: 0; }
  html, body { width: 997px; height: 1200px; overflow: hidden; }
  body { background: var(--board); font-family: "Open Sans", sans-serif; position: relative; }

  .side-label { position: absolute; left: 60px; color: var(--white); font-weight: 600; font-size: 15px; font-family: "Open Sans", sans-serif; }
  .side-label--front { top: 250px; }
  .side-label--back { top: 870px; }

  .sheet { position: absolute; left: 144px; width: 767px; height: 542px; overflow: hidden; background: var(--paper); }
  .sheet--front { top: 39px; }
  .sheet--back { top: 614px; }
  .abs { position: absolute; }

  /* FRONT */
  .photo-team { left: 0; top: 0; width: 193px; height: 336px; background: linear-gradient(160deg, #5a6470 0%, #c9ced4 45%, #eef0f2 100%); }
  .intro { left: 193px; top: 0; width: 191px; height: 336px; background: var(--paper); padding: 14px 14px 0 14px; }
  .intro__tagline { font-style: italic; color: var(--brand-blue); font-size: 12.2px; line-height: 17.5px; }
  .intro__body { margin-top: 26px; font-size: 9.6px; line-height: 13.6px; color: var(--body-ink); text-align: justify; }
  .photo-city { left: 384px; top: 0; width: 383px; height: 542px; background: linear-gradient(180deg, #5a86c4 0%, #9fb6d6 30%, #6d7a94 55%, #3d4e74 72%, #2b4f8c 100%); }
  .logo-block { left: 596px; top: 14px; width: 145px; height: 110px; background: var(--night); display: flex; align-items: flex-end; justify-content: center; padding-bottom: 16px; }
  .logo-block__name { font-family: "Oswald", sans-serif; font-weight: 400; font-size: 14px; color: var(--white); letter-spacing: 0.5px; text-transform: uppercase; }

  .contact-band { left: 0; top: 336px; width: 611px; height: 167px; background: var(--brand-blue); border-top: 6px solid var(--deep-blue); }
  .contact-list { position: absolute; left: 28px; top: 26px; list-style: none; color: var(--white); font-size: 10.4px; }
  .contact-list li { display: flex; align-items: flex-start; margin-bottom: 9px; line-height: 14.5px; }
  .contact-list svg { width: 16px; height: 16px; margin-right: 9px; flex: none; }
  .partner-name { position: absolute; left: 236px; top: 86px; width: 130px; color: var(--white); font-family: "Oswald", sans-serif; font-weight: 400; font-size: 15px; line-height: 17px; }
  .partner-note { display: block; font-family: "Open Sans", sans-serif; font-size: 6px; line-height: 9px; margin-top: 2px; }
  .services { position: absolute; left: 407px; top: 36px; list-style: none; }
  .services li { font-family: "Oswald", sans-serif; font-weight: 400; font-size: 22.5px; color: var(--white); line-height: 34.5px; text-transform: uppercase; }

  .web-strip { left: 0; top: 503px; width: 384px; height: 39px; background: linear-gradient(180deg, #ffffff, #e4e5e7); display: flex; align-items: center; justify-content: center; font-size: 14px; color: var(--ink); }
  .web-overlay { left: 384px; top: 503px; width: 383px; height: 39px; display: flex; align-items: center; justify-content: flex-end; padding-right: 16px; font-size: 14px; color: var(--white); }

  /* BACK */
  .panel-light { left: 0; top: 0; width: 384px; height: 357px; background: linear-gradient(180deg, #f3f4f5, #e3e5e8); }
  .section-title { font-family: "Oswald", sans-serif; font-weight: 400; font-size: 23px; line-height: 28px; text-transform: uppercase; color: var(--ink); white-space: nowrap; }
  .section-title .accent { color: var(--brand-blue); }
  .section-rule { height: 3px; background: var(--ink); }
  .copy { font-size: 9.4px; line-height: 12.4px; text-align: justify; color: var(--body-ink); }
  .copy p + p { margin-top: 11px; }

  .succession-title { left: 21px; top: 22px; }
  .succession-rule { left: 21px; top: 56px; width: 342px; }
  .succession-copy { left: 21px; top: 70px; width: 342px; }
  .quote-box { left: 21px; top: 196px; width: 167px; height: 140px; background: var(--brand-blue); padding: 12px 14px 0 24px; font-style: italic; font-size: 11.5px; line-height: 15.5px; color: var(--white); }
  .quote-mark { position: absolute; font-family: "Georgia", serif; font-size: 24px; color: rgba(255,255,255,0.55); line-height: 1; }
  .growth-graphic { left: 195px; top: 186px; width: 178px; height: 152px; background: radial-gradient(ellipse at 62% 60%, #cfe5b8 0%, #e8eef0 55%, #eaecee 100%); }

  .feature-band { left: 0; top: 357px; width: 384px; height: 4px; background: var(--brand-blue); }
  .photo-growth { left: 0; top: 361px; width: 384px; height: 181px; background: linear-gradient(120deg, #6e7888 0%, #b9c0c8 45%, #2a3346 100%); }
  .caption { left: 0; top: 502px; width: 384px; height: 40px; background: rgba(20,24,34,0.82); color: var(--white); font-style: italic; font-size: 9.8px; line-height: 13px; padding: 5px 20px 0 25px; }

  .panel-blue { left: 384px; top: 0; width: 383px; height: 270px; background: linear-gradient(160deg, #3d7fc0 0%, #2c68a8 100%); }
  .benefits-title { left: 407px; top: 22px; color: var(--white); }
  .benefits-rule { left: 407px; top: 56px; width: 342px; background: var(--white); }
  .benefits-copy { left: 407px; top: 70px; width: 342px; color: var(--white); }
  .benefit-icon { top: 189px; width: 68px; height: 68px; }

  .panel-grey { left: 384px; top: 270px; width: 383px; height: 272px; background: linear-gradient(180deg, #f5f6f7, #dfe1e4); }
  .insurance-title { left: 407px; top: 286px; }
  .insurance-rule { left: 404px; top: 320px; width: 343px; }
  .photo-savings { left: 412px; top: 335px; width: 131px; height: 185px; background: radial-gradient(ellipse at 50% 68%, #f2b7ae 0%, #e9a79f 35%, #e6e7e9 70%); }
  .point-list { position: absolute; left: 561px; top: 339px; width: 186px; list-style: none; }
  .point-list li { display: flex; align-items: flex-start; height: 48.5px; }
  .point-num { flex: none; width: 19px; height: 19px; border-radius: 50%; background: var(--ink); color: var(--white); font-size: 10px; font-weight: 600; display: flex; align-items: center; justify-content: center; margin-right: 10px; margin-top: 1px; }
  .point-text { font-size: 9.4px; line-height: 12px; text-align: justify; color: var(--body-ink); }
</style>
</head>
<body>

<div class="side-label side-label--front">Front</div>
<div class="side-label side-label--back">Back</div>

<section class="sheet sheet--front">
  <div class="abs photo-team" role="img" aria-label="Photo of business consultants gathered around a laptop in an office"></div>

  <div class="abs intro">
    <p class="intro__tagline">Our strong parentage, experienced consultants and commitment to service excellence set us apart from the rest.</p>
    <p class="intro__body">Lorem ipsum dolor sit amet, consectetuer adipiscing elit, sed diam nonummy nibh euismod tincidunt ut laoreet dolore magna aliquam erat volutpat. Ut wisi enim ad minim veniam, quis nostrud exerci tation ullamcorper suscipit lobortis nisl ut aliquip ex ea commodo consequat. Duis autem vel eum iriure dolor in hendrerit in vulputate velit esse molestie consequat, vel ill</p>
  </div>

  <div class="abs photo-city" role="img" aria-label="Photo of a city skyline at dusk reflected in the harbour"></div>

  <div class="abs logo-block">
    <span class="logo-block__name">Planners' Circlet</span>
  </div>

  <div class="abs contact-band">
    <ul class="contact-list">
      <li>
        <svg viewBox="0 0 16 16"><circle cx="8" cy="8" r="7" fill="none" stroke="#fff" stroke-width="1.3"/><path d="M5.5 4.5l1.5 0 .6 1.8-1 .8a5 5 0 002.3 2.3l.8-1 1.8.6 0 1.5c-3.6.3-6.3-2.4-6-6z" fill="#fff"/></svg>
        +65 6200 1845
      </li>
      <li>
        <svg viewBox="0 0 16 16"><circle cx="8" cy="8" r="7" fill="none" stroke="#fff" stroke-width="1.3"/><path d="M5.5 4.5l1.5 0 .6 1.8-1 .8a5 5 0 002.3 2.3l.8-1 1.8.6 0 1.5c-3.6.3-6.3-2.4-6-6z" fill="#fff"/></svg>
        +65 6200 1846
      </li>
      <li>
        <svg viewBox="0 0 16 16"><circle cx="8" cy="8" r="7" fill="none" stroke="#fff" stroke-width="1.3"/><rect x="4.3" y="5.5" width="7.4" height="5" fill="#fff"/><path d="M4.3 5.5l3.7 2.8 3.7-2.8" fill="none" stroke="#3377b5" stroke-width="0.9"/></svg>
        info@plannerscirclet.com.sg
      </li>
      <li>
        <svg viewBox="0 0 16 16"><circle cx="8" cy="8" r="7" fill="none" stroke="#fff" stroke-width="1.3"/><path d="M8 12.5s-3-3.4-3-5.6a3 3 0 016 0c0 2.2-3 5.6-3 5.6z" fill="#fff"/><circle cx="8" cy="6.9" r="1.1" fill="#3377b5"/></svg>
        <span>Harbourline Centre<br>8 Keppel Quay<br>Singapore 098765</span>
      </li>
    </ul>

    <div class="partner-name">Silver Harbour Wealth Planners<span class="partner-note">A member of the Harbour Group</span></div>

    <ul class="services">
      <li>Business Succession</li>
      <li>Employee Benefits</li>
      <li>Corporate Insurance</li>
    </ul>
  </div>

  <div class="abs web-strip">plannerscirclet.com.sg</div>
  <div class="abs web-overlay">plannerscirclet.com.sg</div>
</section>

<section class="sheet sheet--back">
  <div class="abs panel-light"></div>

  <h2 class="abs section-title succession-title"><span class="accent">Business</span> Succession</h2>
  <div class="abs section-rule succession-rule"></div>
  <div class="abs copy succession-copy">
    <p>Lorem ipsum dolor sit amet, consectetuer adipiscing elit, sed diam nonummy nibh euismod tincidunt ut laoreet dolore magna aliquam erat volutpat.</p>
    <p>Ut wisi enim ad minim veniam, quis nostrud exerci tation ullamcorper suscipit lobortis nisl ut aliquip ex ea commodo consequat. Duis autem vel eum iriure dolor in hendrerit in vulputate velit esse molestie consequat, vel illum dolore eu feugiat nulla faci praesent luptatum zzril delenit augue duis dolore te feugait nulla facilisi.</p>
  </div>

  <blockquote class="abs quote-box">
    <span class="quote-mark" style="left:7px;top:8px;">&ldquo;</span>
    Lorem ipsum dolor sit amet, consectetuer adipiscing elit, sed diam nonummy nibh euismod tincidunt ut laoreet dolore magna aliquam erat volutpat.
    <span class="quote-mark" style="right:6px;bottom:-4px;">&rdquo;</span>
  </blockquote>

  <div class="abs growth-graphic" role="img" aria-label="Illustration of a rising 3D bar chart with a green upward arrow"></div>

  <div class="abs feature-band"></div>
  <div class="abs photo-growth" role="img" aria-label="Photo of a businessman drawing rising arrows on a board"></div>
  <p class="abs caption">Lorem ipsum dolor sit amet, consectetuer adipiscing elit, sed diam nonummy nibh euismod tincidunt ut.</p>

  <div class="abs panel-blue"></div>
  <h2 class="abs section-title benefits-title">Employee Benefits</h2>
  <div class="abs section-rule benefits-rule"></div>
  <div class="abs copy benefits-copy">
    <p>Lorem ipsum dolor sit amet, consectetuer adipiscing elit, sed diam nonummy nibh euismod tincidunt ut laoreet dolore magna aliquam erat volutpat.</p>
    <p>Ut wisi enim ad minim veniam, quis nostrud exerci tation ullamcorper suscipit lobortis nisl ut aliquip ex ea commodo consequat. Duis autem vel eum iriure dolor in hendrerit in vulputate velit esse molestie consequat, vel illum dolore eu feugiat nulla faci praesent luptatum zzril delenit augue duis dolore te feugait nulla facilisi.</p>
  </div>

  <svg class="abs benefit-icon" style="left:411px" viewBox="0 0 68 68" aria-hidden="true">
    <circle cx="34" cy="34" r="32" fill="none" stroke="#fff" stroke-width="2"/>
    <rect x="19" y="24" width="26" height="16" fill="none" stroke="#fff" stroke-width="2.4"/>
    <rect x="24" y="29" width="26" height="16" fill="#2f6dae" stroke="#fff" stroke-width="2.4"/>
    <circle cx="37" cy="37" r="4" fill="none" stroke="#fff" stroke-width="2"/>
  </svg>
  <svg class="abs benefit-icon" style="left:501px" viewBox="0 0 68 68" aria-hidden="true">
    <circle cx="34" cy="34" r="32" fill="none" stroke="#fff" stroke-width="2"/>
    <rect x="19" y="21" width="26" height="24" fill="none" stroke="#fff" stroke-width="2.4"/>
    <line x1="19" y1="28" x2="45" y2="28" stroke="#fff" stroke-width="2.4"/>
    <rect x="23" y="32" width="4" height="4" fill="#fff"/><rect x="30" y="32" width="4" height="4" fill="#fff"/><rect x="23" y="38" width="4" height="4" fill="#fff"/>
    <circle cx="44" cy="44" r="7" fill="#2f6dae" stroke="#fff" stroke-width="2.2"/>
    <path d="M44 40v4h3" fill="none" stroke="#fff" stroke-width="1.8"/>
  </svg>
  <svg class="abs benefit-icon" style="left:586px" viewBox="0 0 68 68" aria-hidden="true">
    <circle cx="34" cy="34" r="32" fill="none" stroke="#fff" stroke-width="2"/>
    <path d="M20 19v29h29" fill="none" stroke="#fff" stroke-width="2.4"/>
    <path d="M24 42l7-9 6 5 9-12" fill="none" stroke="#fff" stroke-width="2.2"/>
    <circle cx="31" cy="33" r="2" fill="#fff"/><circle cx="37" cy="38" r="2" fill="#fff"/><circle cx="46" cy="26" r="2" fill="#fff"/>
  </svg>
  <svg class="abs benefit-icon" style="left:672px" viewBox="0 0 68 68" aria-hidden="true">
    <circle cx="34" cy="34" r="32" fill="none" stroke="#fff" stroke-width="2"/>
    <path d="M24 19h20v28a4 4 0 01-4 4H20v-4h4z" fill="none" stroke="#fff" stroke-width="2.4"/>
    <line x1="29" y1="26" x2="40" y2="26" stroke="#fff" stroke-width="2"/>
    <line x1="29" y1="32" x2="40" y2="32" stroke="#fff" stroke-width="2"/>
    <line x1="29" y1="38" x2="40" y2="38" stroke="#fff" stroke-width="2"/>
  </svg>

  <div class="abs panel-grey"></div>
  <h2 class="abs section-title insurance-title"><span class="accent">Corporate</span> Business Insurance</h2>
  <div class="abs section-rule insurance-rule"></div>
  <div class="abs photo-savings" role="img" aria-label="Photo of coins dropping into a pink piggy bank"></div>

  <ol class="point-list">
    <li><span class="point-num">1</span><span class="point-text">Lorem ipsum dolor sit amet, consectetuer adipiscing elit, sed diam nonummy.</span></li>
    <li><span class="point-num">2</span><span class="point-text">Lorem ipsum dolor sit amet, consectetuer adipiscing elit, sed diam nonummy.</span></li>
    <li><span class="point-num">3</span><span class="point-text">Lorem ipsum dolor sit amet, consectetuer adipiscing elit, sed diam nonummy.</span></li>
    <li><span class="point-num">4</span><span class="point-text">Lorem ipsum dolor sit amet, consectetuer adipiscing elit, sed diam nonummy.</span></li>
  </ol>
</section>

</body>
</html>
```